New design for a physiotherapy clinic specializing in laser therapy

BrightPath Physiotherapy is a unique clinic specializing in laser therapy. The clinic is now 7 years old and has a well established reputation for patient care.

We are the largest laser physiotherapy clinic in Mississauga, ON, Canada. We use state of the art laser therapy equipment. Our knowledge base of how to use Low Level Laser Therapy in conjunction with traditional physiotherapy is what sets us apart. Nobody wants to live with pain and everyone wants to get better as quickly as possible. Our treatment methodology helps our patients return to normal lives quickly.

We want a website that communicates expertise, trust and shows that we care for our patients. We also want people to understand that the treatments are painless and speed up healing naturally.
Updates

Please include a location tab in your submission.  This page should have a map of our location and our phone number.

I do not want any white coat and stethoscope people. We do not see hospitalized patients. We use Zorva-Kel NuvaQuill laser web site www.nuvaquilllaser.example please remove any images with other laser machines. I do not want "massage" therapy pictures as the main image. We treat post op total hip and knee replacements, rotator cuff injuries, osteoarthritic back pain patients, sprained ankles, degenerative disc disease problems as some of the more general injuries seen.

Industry/Entity Type

Clinic

Requirements
Must have
• We want to retain as much of the current content as possible. We will be looking at editing the content to make it shorter.

In addition to the current pages we want to add a blog page and link.

see our current site www.brightpathphysio.example
Nice to have
• Medical Images in the Whiplash and Auto Injuries should be re-drawn.

We want a clean, uncluttered look to the site.

Should not have
• Do not use illustrations of lasers shooting out or cutting. This is a "Cold" laser and does not cut. The laser procedure is gentle and soothing.

```html
<!DOCTYPE html>
<html lang="en">
<head>
<meta charset="utf-8">
<title>BrightPath Physiotherapy</title>
<link href="https://fonts.googleapis.com/css2?family=Arimo:ital,wght@0,400;0,700;1,400&display=swap" rel="stylesheet">
<style>
:root{
  --page:#e9f1e2;
  --white:#ffffff;
  --panel:#f8f8f8;
  --green:#76bc3e;
  --ink:#222222;
  --body:#333333;
  --muted:#8a8a8a;
  --line:#dcdcdc;
}
*{box-sizing:border-box;margin:0;padding:0}
html,body{width:893px;height:1200px;overflow:hidden;background:var(--page)}
body{font-family:"Arimo",Arial,sans-serif;color:var(--body)}
.site{width:1100px;height:1478px;transform:scale(0.81182);transform-origin:0 0;position:relative}
.header{position:absolute;left:50px;top:0;width:1004px;height:99px;background:var(--white)}
.brand{position:absolute;left:40px;top:30px;display:flex;align-items:center;gap:10px}
.brand-dot{width:18px;height:18px;border-radius:50%;background:var(--green)}
.brand-name{font-size:21px;letter-spacing:1.5px;color:#2b2b2b;font-weight:400}
.brand-motto{position:absolute;left:132px;top:72px;font-size:14px;color:var(--green)}
.promise{position:absolute;left:523px;top:30px;width:450px;font-style:italic;font-size:18px;line-height:22px;color:var(--muted)}
.nav{position:absolute;left:50px;top:112px;width:1000px;height:47px;background:var(--green)}
.nav ul{list-style:none;display:flex;height:100%}
.nav li{font-size:12.5px;font-weight:700;color:var(--white);line-height:47px;padding:0 13px}
.nav li.active{background:var(--white);color:var(--ink);padding:0 16px 0 24px}
.search{position:absolute;left:774px;top:11px;width:227px;height:25px;background:var(--white);border:1px solid var(--line);font-size:13px;color:#b5b5b5;padding:4px 12px}
.hero-rule{position:absolute;left:50px;width:1000px;height:4px;background:var(--green)}
.hero{position:absolute;left:50px;top:176px;width:1000px;height:508px;background:linear-gradient(100deg,#d9dcb6 0%,#e8c9b3 30%,#b9d39a 55%,#c8a88e 75%,#8fb272 100%)}
.dots{position:absolute;right:32px;bottom:16px;display:flex;gap:8px}
.dots span{width:13px;height:13px;border-radius:50%;background:var(--white)}
.panel{position:absolute;left:52px;width:998px;background:var(--panel)}
h2{font-size:14px;font-weight:700;color:var(--ink);letter-spacing:.2px}
p{font-size:12px;line-height:19px;color:var(--body)}
.more{font-weight:700;color:var(--ink)}
.services{top:688px;height:259px}
.col{position:absolute;top:24px}
.col h2{margin-bottom:16px}
.col p+p{margin-top:19px}
.about{top:962px;height:256px}
.portrait{position:absolute;left:28px;top:61px;width:100px;height:151px;background:linear-gradient(160deg,#b88a6c,#d8c7b4 60%,#8a7a70)}
.video{position:absolute;left:670px;top:40px;width:283px;height:181px;background:linear-gradient(135deg,#c9a47a,#e2ddd3 45%,#9fb6b5 70%,#8d8f93)}
.play{position:absolute;left:128px;top:72px;width:36px;height:36px;border-radius:50%;background:rgba(150,160,170,.75)}
.footer-rule{position:absolute;left:50px;top:1238px;width:1000px;height:4px;background:var(--green)}
.footer{top:1242px;height:225px}
.footer-title{position:absolute;top:23px}
.links{position:absolute;left:23px;top:52px;list-style:none}
.links li{font-size:12px;font-weight:700;letter-spacing:.4px;color:#444;line-height:17px}
.links li:first-child{color:var(--ink)}
.news{position:absolute;left:262px;top:54px;list-style:none}
.news li{font-size:12px;line-height:19px;color:var(--body)}
.map{position:absolute;left:750px;top:52px;width:150px;height:95px;border-radius:50%;background:radial-gradient(ellipse,#e3e9ee,rgba(248,248,248,0) 70%)}
.contact{position:absolute;right:43px;top:23px;text-align:right}
.contact h2{margin-bottom:10px}
.contact p{line-height:19px}
.contact .phones{margin-top:13px;font-weight:700;color:#555}
.social{position:absolute;right:43px;top:166px;display:flex;gap:4px}
.social span{width:32px;height:32px;border-radius:50%}
</style>
</head>
<body>
<div class="site">
  <header class="header">
    <div class="brand"><span class="brand-dot"></span><span class="brand-name">BrightPath Physiotherapy Inc.</span></div>
    <div class="brand-motto">Treating You Better</div>
    <p class="promise">BrightPath Physiotherapy is committed to helping you get better, faster, with fewer treatments.</p>
  </header>

  <nav class="nav">
    <ul>
      <li class="active">HOME</li><li>CLINIC HOURS</li><li>THERAPHY</li><li>WHIPLASH &amp; AUTO INJURIES</li><li>NEWS</li><li>LOCATION</li><li>BLOG</li>
    </ul>
    <div class="search">Search</div>
  </nav>

  <div class="hero-rule" style="top:172px"></div>
  <div class="hero" role="img" aria-label="Smiling family of four outdoors, parents carrying their children piggyback">
    <div class="dots"><span></span><span></span><span></span><span></span><span></span></div>
  </div>
  <div class="hero-rule" style="top:684px"></div>

  <section class="panel services">
    <div class="col" style="left:36px;width:466px">
      <h2>PHYSIOTHERAPHY</h2>
      <p>Physiotherapists are licensed healthcare providers and are dedicated to improving and maintaining functional independence and physical performance. By preventing and managing pain, physical impairments, disabilities and limits to participation, physiotherapists are able to promote fitness, health and wellness.</p>
      <p>Through assessment, treatment and education, physiotherapists can recommend the best way to treat your muscles, bones, joints, circulatory, respiratory or nervous system problems.<br><span class="more">Read more..</span></p>
    </div>
    <div class="col" style="left:537px;width:442px">
      <h2>LOW INTENSITY LASER THERAPY (LILT)</h2>
      <p>LILT is the application of super luminous and laser diodes for the reduction and elimination of pain for a variety of medical conditions. LILT utilizes light energy to stimulate tissue for the purpose of regeneration, improved circulation and accelerated healing.</p>
      <p>This therapy is non invasive, easily applied, painless and very effective. LILT is the latest technological advancement available in passive modality intervention today. Through extensive research and clinical practice we have found that the use of LILT with traditional physiotherapy techniques yields superior results. <span class="more">Read more..</span></p>
    </div>
  </section>

  <section class="panel about">
    <h2 style="position:absolute;left:26px;top:27px">WHO WE ARE</h2>
    <div class="portrait" role="img" aria-label="Portrait of the clinic's lead physiotherapist"></div>
    <p style="position:absolute;left:151px;top:62px;width:515px">We are Mississauga's premier physiotherapy and low intensity laser therapy specialists. We integrate low intensity laser therapy (laser therapy or cold laser therapy) with physiotherapy to safely and effectively treat a wide variety of musculoskeletal injuries and inflammatory conditions (i.e. back pain, arthritis, knee injuries, shoulder injuries, tendonitis, bursitis, repetitive strains, auto &amp; sports injuries). We Use a multi-faceted regime of clinically tested and proven protocols with one goal in mind: Get you better, faster.<br><span class="more">Read more..</span></p>
    <h2 style="position:absolute;left:668px;top:19px">TESTIMONIALS</h2>
    <div class="video" role="img" aria-label="Video still of a therapist with a patient in the clinic"><span class="play"></span></div>
    <p style="position:absolute;left:670px;top:228px;font-size:14px">Watch Video</p>
  </section>

  <div class="footer-rule"></div>
  <footer class="panel footer">
    <h2 class="footer-title" style="left:21px">QUICK LINKS</h2>
    <ul class="links">
      <li>HOME</li><li>CLINIC HOURS</li><li>PHYSIOTHERAPHY</li><li>LASER THERAPHY</li><li>WHIPLASH &amp; AUTO INJURIES</li><li>NEWS</li><li>MASSAGE THERAPHY</li><li>LOCATION</li><li>BLOG</li>
    </ul>
    <h2 class="footer-title" style="left:262px">IN THE NEWS</h2>
    <ul class="news">
      <li>Drug Free Pain Relief</li>
      <li>End Joint and Back Pain - A Patient's Road to Recovery</li>
      <li>Low Intensity Laser For Pain Relief</li>
      <li>Suffering From Arthritis? Try a Light Touch</li>
      <li>Physiotherapy &amp; Laser Therapy For Neck Pain &amp; Whiplash</li>
    </ul>
    <div class="map" role="img" aria-label="Faint world map backdrop"></div>
    <div class="contact">
      <h2>CONTACT DETAILS</h2>
      <p>Maplewood Centre<br>1480 Cedar Grove Parkway<br>Mississauga, ON L5M 2B7</p>
      <p class="phones">Telephone: 905-555-0142<br>FAX: 905-555-0178</p>
    </div>
    <div class="social">
      <span style="background:#e8631c"></span><span style="background:#c9382b"></span><span style="background:#3b5a9a"></span><span style="background:#2fa6e0"></span>
    </div>
  </footer>
</div>
</body>
</html>
```